Client Meeting and installation Email Follow up

I would like a follow-up email template created.
Currently, we do a lot of new construction builds and meet with clients about 6-3 months before they take possession of their new house. I want a follow-up email template to be sent after the homeowner takes possession of their house that enquires if the clients are happy about their new lighting, the service they received, and their customer service representative with Meridale Glow and Breeze. I have attached a few files of what our current marketing looks like.
Target Market(s)
Home Owners We have already met with
Industry/Entity Type
Residential lighting
Font styles to use
Other font styles liked:
- Alta Light, Playfair Display, Montserrat
Colors
Designer to choose colors to be used in the design.
Look and feel
Each slider illustrates characteristics of the customer's brand and the style your logo design should communicate.

```html
<!DOCTYPE html>
<html lang="en">
<head>
<meta charset="utf-8">
<title>Meridale Glow and Breeze – Installation Follow-Up</title>
<link href="https://fonts.googleapis.com/css2?family=Josefin+Sans:wght@400;600;700&display=swap" rel="stylesheet">
<style>
:root{
  --brown:#9b7a67;
  --brown-dark:#8a6b59;
  --ink:#1b1b1b;
  --paper:#f6f4f3;
  --slate:#5c6270;
  --footer:#3d3c3f;
  --white:#ffffff;
}
*{margin:0;padding:0;box-sizing:border-box}
html,body{width:1200px;height:3756px;overflow:hidden}
body{font-family:"Josefin Sans",sans-serif;color:var(--ink);background:var(--paper);position:relative}
.abs{position:absolute}
.hero-top{left:0;top:0;width:1200px;height:690px;background:linear-gradient(180deg,#5d6372 0%,#6f7482 55%,#565b68 100%)}
.hero-bottom{left:0;top:0;width:1200px;height:1146px}
.brand{left:78px;top:44px;color:var(--white);font-weight:600;font-size:44px;letter-spacing:1px;line-height:1.1}
.hero-title{left:78px;top:255px;color:var(--white);font-weight:700;font-size:64px;line-height:80px;letter-spacing:2px}
.intro{left:0;top:1146px;width:1200px;height:210px;background:var(--brown);color:var(--white);font-size:25px;line-height:37.5px;text-align:center;padding:37px 70px 0;letter-spacing:.5px}
.section-title{left:0;top:1425px;width:1200px;text-align:center;font-weight:600;line-height:69px;letter-spacing:2px}
.section-title .l1{font-size:48px}
.section-title .l2{font-size:54px}
.item-title{font-size:37px;line-height:54px;letter-spacing:1.5px}
.item-title .accent{color:var(--brown);font-weight:600;text-decoration:underline;text-underline-offset:6px;text-decoration-thickness:2px}
.item-body{font-size:26px;line-height:48px;letter-spacing:.6px}
.pill{height:33px;border-radius:0 6px 6px 0;background:var(--brown);color:var(--white);font-size:22px;font-weight:600;letter-spacing:1.5px;padding:6px 0 0 22px}
.closing{left:0;top:3180px;width:1200px;text-align:center;color:var(--white);font-size:33px;line-height:52px;letter-spacing:1px}
.closing p+p{margin-top:24px}
.footer{left:0;top:3540px;width:1200px;height:216px;background:var(--footer)}
.footer-brand{left:80px;top:3603px;color:var(--white);font-weight:600;font-size:30px;letter-spacing:1px;line-height:1.1}
.social{top:3628px;width:30px;height:30px;border-radius:4px}
.rule{left:76px;top:3709px;width:1046px;height:2px;background:var(--white)}
.copyright{left:0;top:3726px;width:1200px;text-align:center;color:var(--white);font-size:15px}
.code{left:1152px;top:3718px;color:var(--white);font-size:14px}
</style>
</head>
<body>

<svg class="abs hero-bottom" width="1200" height="1146" viewBox="0 0 1200 1146">
  <defs>
    <linearGradient id="roomGrey" x1="0" y1="0" x2="1" y2="1">
      <stop offset="0" stop-color="#e6e6e4"/>
      <stop offset=".5" stop-color="#b8b9b6"/>
      <stop offset="1" stop-color="#d9d8d4"/>
    </linearGradient>
  </defs>
  <rect width="1200" height="1146" fill="url(#roomGrey)" role="img" aria-label="Dining room with a round floral chandelier, round mirror and palm mural"/>
</svg>
<div class="abs hero-top" role="img" aria-label="Slate blue dining room with a globe chandelier, tulips and blue chairs" style="clip-path:polygon(0 0,1200px 0,1200px 578px,0 690px)"></div>

<div class="abs brand">MERIDALE<br>GLOW &amp; BREEZE</div>
<h1 class="abs hero-title">We Hope You’re Loving<br>Your New Lighting!</h1>

<p class="abs intro">Congratulations on the recent move into your new home! We hope you’re settling in well and enjoying your new space. At Meridale Glow and Breeze, we’re dedicated to ensuring that every detail of your lighting installation meets your expectations. We’d love to hear about your experience with our services and the installation process.</p>

<h2 class="abs section-title"><span class="l1">Here Are a Few Things We’d</span><br><span class="l2">Appreciate Your Feedback On</span></h2>

<!-- Lighting satisfaction -->
<h3 class="abs item-title" style="left:78px;top:1665px">Your Satisfaction With<br>The <span class="accent">Lighting:</span></h3>
<p class="abs item-body" style="left:78px;top:1800px;width:590px">Are you pleased with how the lighting enhances your new home? Are there any adjustments or additional features you would like to discuss?</p>

<svg class="abs" style="left:740px;top:1600px" width="460" height="610" viewBox="740 1600 460 610">
  <circle cx="1072" cy="1897" r="240" fill="var(--brown)"/>
  <circle cx="1072" cy="1897" r="224" fill="#e9e9e8" role="img" aria-label="White kitchen with pendant lights"/>
  <circle cx="937" cy="1692" r="75" fill="var(--brown)"/><circle cx="937" cy="1692" r="69" fill="#f8f8f8" role="img" aria-label="Black chandelier with white globes"/>
  <circle cx="843" cy="1857" r="87" fill="var(--brown)"/><circle cx="843" cy="1857" r="81" fill="#f8f8f8" role="img" aria-label="Drum pendant light"/>
  <circle cx="861" cy="2026" r="75" fill="var(--brown)"/><circle cx="861" cy="2026" r="69" fill="#f8f8f8" role="img" aria-label="LED disc light"/>
  <circle cx="1005" cy="2120" r="75" fill="var(--brown)"/><circle cx="1005" cy="2120" r="69" fill="#f8f8f8" role="img" aria-label="Single globe pendant"/>
</svg>
<div class="abs pill" style="left:1005px;top:1720px;width:128px">NOOK</div>
<div class="abs pill" style="left:925px;top:1854px;width:175px">STAIRWAY</div>
<div class="abs pill" style="left:940px;top:1974px;width:175px">LED DISC</div>
<div class="abs pill" style="left:1058px;top:2044px;width:142px">PENDANT</div>

<!-- Installation -->
<svg class="abs" style="left:0;top:2050px" width="450" height="570" viewBox="0 2050 450 570">
  <circle cx="165" cy="2336" r="280" fill="var(--brown)"/>
  <circle cx="165" cy="2336" r="262" fill="#c9c2b8" role="img" aria-label="Open kitchen and dining area with a crystal chandelier"/>
</svg>
<h3 class="abs item-title" style="left:518px;top:2248px">The <span class="accent">Installation Process:</span></h3>
<p class="abs item-body" style="left:518px;top:2326px;width:520px">Did our team meet your expectations during the installation? Was the process smooth and professional?</p>

<!-- Customer service -->
<h3 class="abs item-title" style="left:81px;top:2712px">Customer <span class="accent">Service Experience:</span></h3>
<p class="abs item-body" style="left:83px;top:2790px;width:520px;line-height:42px">How did you find working with your Meridale Glow and Breeze representative? Were they helpful and responsive to your needs?</p>
<svg class="abs" style="left:745px;top:2480px" width="455" height="580" viewBox="745 2480 455 580">
  <circle cx="1035" cy="2775" r="285" fill="var(--brown)"/>
  <circle cx="1035" cy="2775" r="268" fill="#b9c3d4" role="img" aria-label="Installer fitting a ceiling light"/>
</svg>

<!-- Closing band -->
<div class="abs" style="left:0;top:3004px;width:1200px;height:536px;background:var(--brown);clip-path:polygon(0 0,1200px 94px,1200px 536px,0 536px)"></div>
<div class="abs closing">
  <p>Your feedback is invaluable to us as it helps us continually<br>improve our services. If there’s anything you’d like to discuss or if<br>you need further assistance, please don’t hesitate to reach out.</p>
  <p>Thank you for choosing Meridale Glow and Breeze for your<br>new home. We look forward to hearing from you and hope you<br>continue to enjoy your beautifully lit space!</p>
</div>

<!-- Footer -->
<div class="abs footer"></div>
<div class="abs footer-brand">MERIDALE<br>GLOW &amp; BREEZE</div>
<div class="abs social" style="left:943px;background:#1877f2"></div>
<div class="abs social" style="left:980px;background:#ffffff"></div>
<div class="abs social" style="left:1017px;background:#e60023"></div>
<div class="abs social" style="left:1054px;background:#d6249f"></div>
<div class="abs social" style="left:1091px;background:#ff0000"></div>
<div class="abs rule"></div>
<p class="abs copyright">Copyright © 2024 Meridale Glow &amp; Breeze. All rights reserved.</p>
<p class="abs code">C67</p>
</body>
</html>
```